Webdesign für Verkauf, Installation, Instandsetzung und Wartung von Tafelwasseranlagen
Zielgruppe
Verkauf, Installation, Instandsetzung und Wartung von Tafelwasseranlagen, Der Firmenname soll Seeperle heissen
Aufgabenstellung
Da es um Wasser geht sollte blau schon mit dabei sein, ein Logo wäre nicht schlecht. Da ich die Tafelwassersäulen verkaufen möchte kann ich diese Foto im nachhinein anbieten.
ich dachte an Startseite, über Uns , Wasserspender, Kontakt und Impresum.
Es handelt sich um Wassersäulen und Untertischgeröten von Hevanto, Hersteller habe ich schon angefragt aber noch keine definitive Zusage von Fotos und Texte bekommen. Ansonsten müsste man über meinen Großhändler gehen.
Es betrifft eher die Geschäftskunden, ich denke Privatkunden würde es sich nicht rechnen, da gibt es ja den Perlquix.
Es werden mehrere Wasserspender angeboten und werden auch vermietet.
Preise werden im Internet für Tafelwasser Geräte nicht angeboten, dafür muss ein Interessent eine Anfrage stellen.
Texte und Logodesign werden extra in Auftrag gegeben, Wasserspender von Olvena werden nicht in Frage kommen sind zu teuer auch in der Wartung.
Bekanntheit erst mal in der Region Bodensee, wenn es besser läuft deutschlandweit

```html
<!DOCTYPE html>
<html lang="de">
<head>
<meta charset="utf-8">
<title>Seeperle – Startseite</title>
<link href="https://fonts.googleapis.com/css2?family=IBM+Plex+Sans:wght@400;500;600&display=swap" rel="stylesheet">
<style>
  :root {
    --bg-light: #d3f8fc;
    --bg-mid: #b4f0f8;
    --bg-deep: #a3e8f6;
    --ink: #13232a;
    --nav-muted: #9fb9c0;
    --accent: #22c8e6;
    --mark: #19c6e0;
  }
  * { margin: 0; padding: 0; box-sizing: border-box; }
  html, body { width: 1200px; height: 1102px; overflow: hidden; }
  body {
    font-family: "IBM Plex Sans", sans-serif;
    color: var(--ink);
    position: relative;
  }
  .backdrop {
    position: absolute; inset: 0;
    background:
      radial-gradient(ellipse 60% 40% at 50% 70%, rgba(140,220,240,0.55), transparent 70%),
      linear-gradient(180deg, var(--bg-mid) 0%, var(--bg-light) 20%, var(--bg-mid) 60%, var(--bg-deep) 100%);
  }
  .site-header {
    position: absolute; top: 22px; left: 89px; right: 37px; height: 52px;
    display: flex; align-items: center; justify-content: space-between;
  }
  .brand { display: flex; align-items: center; gap: 8px; font-size: 16.5px; font-weight: 500; }
  .brand-dot { width: 22px; height: 22px; border-radius: 50%; background: var(--mark); }
  .main-nav { display: flex; gap: 17px; font-size: 13.5px; font-weight: 600; }
  .main-nav a { color: var(--nav-muted); text-decoration: none; padding-bottom: 5px; }
  .main-nav a.active { color: var(--ink); border-bottom: 2px solid var(--accent); }
  .hero {
    position: absolute; top: 157px; left: 0; right: 0;
    display: flex; flex-direction: column; align-items: center; text-align: center;
  }
  .hero-mark { width: 104px; height: 104px; border-radius: 50%; background: var(--mark); opacity: .85; }
  .hero-title { margin-top: 50px; font-size: 34px; font-weight: 500; letter-spacing: .2px; }
  .hero-text { width: 662px; margin-top: 20px; font-size: 13.3px; line-height: 20px; }
  .hero-text + .hero-text { margin-top: 26px; }
  .site-footer { position: absolute; left: 86px; top: 1068px; font-size: 10.5px; }
</style>
</head>
<body>
  <div class="backdrop" role="img" aria-label="Hellblaue Wasseroberfläche mit Tropfen und ringförmigen Wellen"></div>

  <header class="site-header">
    <div class="brand"><span class="brand-dot"></span><span>Seeperle</span></div>
    <nav class="main-nav">
      <a class="active" href="#">Startseite</a>
      <a href="#">Über uns</a>
      <a href="#">Wasserspender</a>
      <a href="#">Kontakt</a>
      <a href="#">Impressum</a>
    </nav>
  </header>

  <main class="hero">
    <div class="hero-mark"></div>
    <h1 class="hero-title">Seeperle</h1>
    <p class="hero-text">Bei Seeperle dreht sich alles um die professionelle Betreuung und Versorgung mit hochwertigen Tafelwasseranlagen. Seit unserer Gründung haben wir uns einen Ruf als zuverlässiger Partner für Verkauf, Installation, Instandsetzung und Wartung von Tafelwasseranlagen erarbeitet. Unser engagiertes Team besteht aus erfahrenen Fachleuten, die sich leidenschaftlich dafür einsetzen, maßgeschneiderte Lösungen anzubieten, die genau auf die Bedürfnisse unserer Kunden zugeschnitten sind. Wir verstehen, dass jede Umgebung unterschiedliche Anforderungen hat, sei es ein Bürogebäude, eine Schule, ein Restaurant oder ein Fitnessstudio. Deshalb arbeiten wir eng mit unseren Kunden zusammen, um sicherzustellen, dass sie die bestmögliche Lösung erhalten. Unser Service umfasst den gesamten Lebenszyklus Ihrer Tafelwasseranlage. Von der ersten Beratung über die Installation bis hin zur regelmäßigen Wartung und schnellen Instandsetzung stehen wir Ihnen mit Fachkenntnissen und Engagement zur Seite. Wir legen großen Wert auf Qualität und Zuverlässigkeit, und daher arbeiten wir nur mit führenden Herstellern zusammen, um sicherzustellen, dass unsere Kunden stets die bestmöglichen Produkte erhalten. Bei Seeperle stehen Kundenzufriedenheit und Servicequalität an erster Stelle. Wir streben danach, langfristige Beziehungen aufzubauen und unseren Kunden einen erstklassigen Service zu bieten, der ihre Erwartungen übertrifft. Kontaktieren Sie uns noch heute, um mehr darüber zu erfahren, wie wir Ihnen bei Ihren Tafelwasseranlagen-Anforderungen helfen können!</p>
    <p class="hero-text">Verkauf, Installation, Instandsetzung und Wartung von Tafelwasseranlagen in der Region des Bodensees. Frisches Trinkwasser aus dem Hahn, gekühlt, gesprudelt oder still. Wir bieten Ihnen die passende Lösung für Ihr Unternehmen. Verlasssen Sie sich auf uns, wir sind Ihr Partner für Wasserspender in der Region Bodensee.</p>
  </main>

  <footer class="site-footer">© 2024 Seeperle | Alle Rechte vorbehalten. (TEMPLATE)</footer>
</body>
</html>
```